Personal Business Card Design Project

I am looking for a business card to be able to hand to both Chinese and Australian businessman.
I am a self employed consultant and just need my name, phone number and email address on the card. No Business Name and No Website.
I want it to look like an exclusive prestigious card.
I would like the background to be be a glossy red and the writing to be gold. (This applies to both sides of the card).
It must have English on one side and Chinese (Mandarin) on the reverse.
Details you will require
Name : Derek Hollins
Phone : + 61 428 903 574
Email : derekhollins@mailvanto.com
Updates
Thank you everybody for your designs.
Industry/Entity Type
Business

```html
<!DOCTYPE html>
<html lang="en">
<head>
<meta charset="utf-8">
<title>Derek Hollins — Business Card</title>
<link rel="stylesheet" href="https://fonts.googleapis.com/css2?family=Cabin+Condensed:wght@600&family=Orbitron:wght@700&family=Cinzel:wght@700&family=Cabin:wght@500&family=Noto+Serif+SC:wght@700&family=Noto+Sans+SC:wght@500&display=swap">
<style>
  :root {
    --red-core: #c8121b;
    --red-mid: #b70f17;
    --red-edge: #9a0d12;
    --gold-ink: #ffe800;
    --corner-gold: #ffee00;
  }
  html, body {
    margin: 0;
    padding: 0;
    width: 1050px;
    height: 1200px;
    overflow: hidden;
    background: #ffffff;
  }
  .sheet {
    position: relative;
    width: 1050px;
    height: 1200px;
  }
  .card-side {
    position: relative;
    width: 1050px;
    height: 600px;
    overflow: hidden;
    color: var(--gold-ink);
  }
  .card-side--front {
    background: radial-gradient(ellipse 70% 75% at 50% 40%, var(--red-core) 0%, var(--red-mid) 55%, var(--red-edge) 100%);
  }
  .card-side--back {
    background: radial-gradient(ellipse 70% 75% at 50% 60%, var(--red-core) 0%, var(--red-mid) 55%, var(--red-edge) 100%);
  }
  .corner {
    position: absolute;
    top: 0;
    right: 0;
    width: 213px;
    height: 195px;
  }
  .side-label {
    position: absolute;
    left: 22px;
    top: 10px;
    margin: 0;
    font-family: "Cabin Condensed", "Gill Sans", sans-serif;
    font-weight: 600;
    font-size: 45px;
    line-height: 1;
  }
  .contact {
    position: absolute;
    left: 10px;
    right: 0;
    top: 210px;
    text-align: center;
  }
  .contact__name {
    margin: 0;
    font-family: "Orbitron", sans-serif;
    font-weight: 700;
    font-size: 64px;
    letter-spacing: 4px;
    line-height: 72px;
  }
  .contact__phone {
    margin: 0;
    font-family: "Cinzel", serif;
    font-weight: 700;
    font-size: 33px;
    letter-spacing: 4px;
    line-height: 46px;
  }
  .contact__email {
    margin: 0;
    font-family: "Cabin", "Gill Sans", sans-serif;
    font-weight: 500;
    font-size: 35px;
    letter-spacing: 1.5px;
    line-height: 42px;
  }
  .contact--zh .contact__name {
    font-family: "Noto Serif SC", serif;
    font-size: 60px;
    letter-spacing: 6px;
  }
  .contact--zh .contact__phone {
    font-family: "Noto Serif SC", serif;
    font-size: 31px;
    letter-spacing: 3px;
  }
  .contact--zh .contact__email {
    font-family: "Noto Sans SC", "Cabin", sans-serif;
    font-size: 33px;
    letter-spacing: 1px;
  }
</style>
</head>
<body>
<main class="sheet">
  <section class="card-side card-side--front">
    <svg class="corner" viewBox="0 0 213 195" aria-hidden="true">
      <polygon points="0,0 213,0 213,195" fill="var(--corner-gold)"/>
    </svg>
    <h2 class="side-label">Front</h2>
    <div class="contact">
      <p class="contact__name">Derek Hollins</p>
      <p class="contact__phone">Phone : + 61 428 903 574</p>
      <p class="contact__email">Email : derekhollins@mailvanto.com</p>
    </div>
  </section>
  <section class="card-side card-side--back">
    <svg class="corner" viewBox="0 0 213 195" aria-hidden="true">
      <polygon points="0,0 213,0 213,195" fill="var(--corner-gold)"/>
    </svg>
    <h2 class="side-label">Back</h2>
    <div class="contact contact--zh" lang="zh-Hans">
      <p class="contact__name">德里克·霍林斯</p>
      <p class="contact__phone">电话 : + 61 428 903 574</p>
      <p class="contact__email">电子邮件 : derekhollins@mailvanto.com</p>
    </div>
  </section>
</main>
</body>
</html>
```